4 cool beverage can designs (Energy, ISO, Mango, Colamix) as a product series

About us
Brinvale Motorsport is an international off-road motorsport team from Switzerland, specialised in the Rally Quorvenne and Quorvenne Heritage. We are producing four drink flavours as printed cans, used as team and event drinks. We are looking for a strong, consistent design in the style of well-known energy brands (think Vortag Fuel): bold, vibrant and instantly recognisable.
The task
Design four can designs (250ml SlimLine) that work together as a clearly recognisable series (same design language, same base layout, same logo placement), while each flavour is clearly distinct from the others. Important: the flavour should be recognisable at first glance, ideally through one clear base colour per flavour.
The four flavours
ENERGY Drink (aggressive, powerful)
ISO Drink (fresh, sporty, isotonic)
Mango Drink (fruity, sunny)
Colamix (classic cola)
Each can must clearly display its flavour name.
Colours (idea only, not fixed)
The colour choice is entirely up to you as the designer. The only requirement is that each flavour gets its own clearly distinguishable colour world and that the flavour is intuitively recognisable. As non-binding inspiration: Energy could be red, ISO blue, Mango orange, Colamix black. Feel free to surprise us with your own bold ideas, as long as the four flavours stay easy to tell apart.
Style and look
Cool, modern, high energy, premium feel in the style of Vortag Fuel, Kestrix, Zonda
Vibrant, punchy colours are explicitly encouraged
Dynamic graphic elements welcome (splashes, claw marks, light streaks, abstract shapes, carbon, energy effects)
A reference to motorsport, rally or desert is allowed but not required (e.g. tyre tracks, speed, off-road). Use it only if it makes the design stronger
The four cans must clearly read as one family when placed side by side
Must include
The Brinvale Motorsport logo, clearly visible and prominently placed (logo file will be provided)
The flavour name, clearly legible (ENERGY, ISO, MANGO, COLAMIX)
Consistent logo position and design system across all four cans
No-gos
The official Quorvenne logo as well as official Quorvenne wordmarks and trademarks must NOT be used for legal reasons (a general motorsport or desert look is fine, just no protected Quorvenne branding)
No pale or pastel colours
No cluttered or overloaded layouts where the logo and flavour name get lost
No designs that only work for a single flavour and do not fit the series
No designs that cannot be technically implemented in the pelvaro.de configurator (see technical specs). Submissions that do not work there will not be considered
Technical specifications (mandatory, production runs via pelvaro.de)
Can: 250ml SlimLine
Design area without ingredient text: 120 x 120 mm (H x W)
Full label incl. ingredients/mandatory info: 170 x 120 mm (H x W)
Resolution: 300 dpi
Colour mode: CMYK (4/0 or 5/0 print)
Keep space free for the deposit label (50 x 25 mm); this area must not be covered by important design elements
Please work exactly within the official pelvaro.de layout template (available at pelvaro.de/de/layoutvorlagen). Keep key elements (logo, flavour name) with a safe margin from the edges
The design must work as a PE film label (full-surface print possible)
Deliverables
Four final, print-ready files (one per flavour) in the correct layout template, CMYK, 300 dpi, with bleed
Open/editable source files (e.g. Adobe Illustrator AI or Photoshop PSD), fonts embedded or converted to outlines
Optional but appreciated: a 3D mockup preview per can
Judging criteria
Instant recognisability of the flavour
Visibility and impact of the Brinvale Motorsport logo
Coolness and recognition in the style of strong energy brands
Consistency as one unified set of four
Technical feasibility in the pelvaro.de configurator
Layout Template https://www.pelvaro.de/en/layoutvorlagen

```html
<!DOCTYPE html>
<html lang="en">
<head>
<meta charset="utf-8">
<title>Brinvale Motorsport – Can Series</title>
<link rel="stylesheet" href="https://fonts.googleapis.com/css2?family=Russo+One&family=Saira+Condensed:wght@700;800&display=swap">
<style>
  :root {
    --stage: #050505;
    --energy-base: #8c1c22;
    --energy-deep: #4a0c10;
    --energy-glow: #ff5a14;
    --iso-base: #1a5fd2;
    --iso-deep: #0b2a6e;
    --iso-glow: #7fd0ff;
    --mango-base: #f28a12;
    --mango-deep: #d25a06;
    --mango-glow: #ffd24a;
    --cola-base: #1b1b1b;
    --cola-deep: #0a0a0a;
    --cola-glow: #c8805a;
    --accent: #ff6a1a;
    --logo-dark: #121212;
    --logo-light: #f2f2f2;
    --flavour-fill: #f4f4f4;
    --flavour-edge: #111111;
    --subtitle: #f4f4f4;
  }
  * { box-sizing: border-box; margin: 0; padding: 0; }
  html, body {
    width: 1200px; height: 896px; overflow: hidden;
    background: var(--stage);
  }
  .series {
    position: relative; width: 1200px; height: 896px;
  }
  .label {
    position: absolute; top: 88px; width: 250px; height: 720px;
    border-radius: 6px; overflow: hidden;
  }
  .label--energy { left: 73px;  background: linear-gradient(180deg, var(--energy-base), var(--energy-deep)); }
  .label--iso    { left: 341px; background: linear-gradient(180deg, var(--iso-base), var(--iso-deep)); }
  .label--mango  { left: 609px; background: linear-gradient(180deg, var(--mango-base), var(--mango-deep)); }
  .label--cola   { left: 877px; background: linear-gradient(180deg, var(--cola-base), var(--cola-deep)); }

  .brand {
    position: absolute; top: 58px; left: 0; right: 0;
    display: flex; align-items: center; justify-content: center; gap: 10px;
  }
  .brand__mark { width: 14px; height: 14px; background: var(--accent); }
  .brand__name {
    font-family: "Russo One", sans-serif; font-weight: 400;
    line-height: 1; text-align: left; color: var(--logo-dark);
  }
  .brand__name span { display: block; }
  .brand__main { font-size: 30px; letter-spacing: 0.5px; }
  .brand__sub { font-size: 13px; letter-spacing: 2.6px; margin-top: 4px; }
  .label--cola .brand__name { color: var(--logo-light); }

  .artwork {
    position: absolute; left: 0; right: 0; top: 170px; height: 460px;
  }
  .label--energy .artwork { background: radial-gradient(ellipse at 55% 50%, rgba(255,90,20,.55), rgba(20,8,8,.35) 60%, transparent 80%); }
  .label--iso .artwork    { background: radial-gradient(ellipse at 50% 45%, rgba(127,208,255,.55), rgba(8,24,70,.5) 60%, transparent 85%); }
  .label--mango .artwork  { background: radial-gradient(ellipse at 50% 50%, rgba(255,210,74,.75), rgba(232,96,10,.45) 60%, transparent 85%); }
  .label--cola .artwork   { background: radial-gradient(ellipse at 50% 50%, rgba(120,120,120,.45), rgba(200,128,90,.18) 60%, transparent 85%); }

  .flavour {
    position: absolute; left: 0; top: 0; width: 250px; height: 720px;
  }
  .flavour text {
    font-family: "Russo One", sans-serif;
    fill: var(--flavour-fill);
    stroke: var(--flavour-edge); stroke-width: 5; paint-order: stroke;
  }
  .frame line { stroke: var(--cola-glow); stroke-width: 3; }

  .subtitle {
    position: absolute; left: 0; right: 0; top: 648px;
    text-align: center; color: var(--subtitle);
    font-family: "Saira Condensed", sans-serif; font-weight: 800;
    font-size: 22px; letter-spacing: 0.5px;
  }
</style>
</head>
<body>
<main class="series">

  <section class="label label--energy">
    <div class="brand"><span class="brand__mark"></span><p class="brand__name"><span class="brand__main">BRINVALE</span><span class="brand__sub">MOTORSPORT</span></p></div>
    <div class="artwork" role="img" aria-label="Orange lightning bolts and claw streaks over carbon fibre"></div>
    <svg class="flavour" viewBox="0 0 250 720" aria-hidden="true">
      <text x="0" y="0" font-size="112" transform="translate(168,630) rotate(-90)" textLength="420" lengthAdjust="spacingAndGlyphs">ENERGY</text>
    </svg>
    <p class="subtitle">ENERGY DRINK</p>
  </section>

  <section class="label label--iso">
    <div class="brand"><span class="brand__mark"></span><p class="brand__name"><span class="brand__main">BRINVALE</span><span class="brand__sub">MOTORSPORT</span></p></div>
    <div class="artwork" role="img" aria-label="Swirling blue water wave splashing across carbon fibre"></div>
    <svg class="flavour" viewBox="0 0 250 720" aria-hidden="true">
      <text x="0" y="0" font-size="138" transform="translate(176,600) rotate(-90)" textLength="300" lengthAdjust="spacingAndGlyphs">ISO</text>
    </svg>
    <p class="subtitle">ISOTONIC DRINK</p>
  </section>

  <section class="label label--mango">
    <div class="brand"><span class="brand__mark"></span><p class="brand__name"><span class="brand__main">BRINVALE</span><span class="brand__sub">MOTORSPORT</span></p></div>
    <div class="artwork" role="img" aria-label="Ripe mango with juice splash and glowing desert sun"></div>
    <svg class="flavour" viewBox="0 0 250 720" aria-hidden="true">
      <text x="0" y="0" font-size="112" transform="translate(168,630) rotate(-90)" textLength="420" lengthAdjust="spacingAndGlyphs">MANGO</text>
    </svg>
    <p class="subtitle">MANGO ENERGY</p>
  </section>

  <section class="label label--cola">
    <div class="brand"><span class="brand__mark"></span><p class="brand__name"><span class="brand__main">BRINVALE</span><span class="brand__sub">MOTORSPORT</span></p></div>
    <div class="artwork" role="img" aria-label="Grey smoke with copper sparks over carbon fibre"></div>
    <svg class="flavour" viewBox="0 0 250 720" aria-hidden="true">
      <g class="frame">
        <line x1="10" y1="250" x2="60" y2="330"/><line x1="60" y1="330" x2="60" y2="480"/><line x1="60" y1="480" x2="10" y2="560"/>
        <line x1="240" y1="250" x2="190" y2="330"/><line x1="190" y1="330" x2="190" y2="480"/><line x1="190" y1="480" x2="240" y2="560"/>
      </g>
      <text x="0" y="0" font-size="104" transform="translate(165,630) rotate(-90)" textLength="440" lengthAdjust="spacingAndGlyphs">COLAMIX</text>
    </svg>
    <p class="subtitle">COLA MIX</p>
  </section>

</main>
</body>
</html>
```